hi all

Im after a new age looking business card with my company logo on it

must include these details, I would like the PH and Email to be symbols

If the colours used for card could be kept within the colours used in logo that I have supplied that would be great, if another colour is to be used dark grey would be ok. no light bulbs etc thanks

Details below to be incorporated on card

Damian Holloway

Lic E871302

PH 0219647381

E info@brightvaleelectrical.example.nz

Domestic Commercial Industrial Electricians

```html
<!DOCTYPE html>
<html lang="en">
<head>
<meta charset="utf-8">
<title>Brightvale Electrical – Business Card</title>
<link rel="stylesheet" href="https://fonts.googleapis.com/css2?family=Montserrat:ital,wght@0,400;0,700;1,700&display=swap">
<style>
  :root {
    --stage: #dcdee1;
    --card: #2b2a29;
    --card-edge: #232221;
    --emblem-dark: #1c1b1b;
    --emblem-mid: #262525;
    --emblem-rim: #3a3939;
    --brand-blue: #1479c9;
    --ink-light: #f2f2f2;
    --ink-muted: #d9d9d9;
  }
  * { box-sizing: border-box; margin: 0; padding: 0; }
  html, body { width: 1200px; height: 800px; overflow: hidden; }
  body {
    background: var(--stage);
    font-family: "Montserrat", Arial, sans-serif;
    display: flex;
    flex-direction: column;
    align-items: center;
    justify-content: center;
    gap: 28px;
  }
  .card {
    position: relative;
    width: 640px;
    height: 366px;
    background: var(--card);
    border: 1px solid var(--card-edge);
    box-shadow: 0 6px 18px rgba(0,0,0,0.25);
    color: var(--ink-light);
    overflow: hidden;
  }
  .emblem-area {
    position: absolute;
    inset: 0;
    width: 100%;
    height: 100%;
  }
  .brand {
    display: flex;
    align-items: center;
    gap: 12px;
    z-index: 1;
  }
  .brand-dot {
    width: 22px; height: 22px;
    border-radius: 50%;
    background: var(--brand-blue);
    flex: none;
  }
  .brand-name {
    color: var(--brand-blue);
    font-weight: 700;
    text-transform: uppercase;
    letter-spacing: 0.05em;
    white-space: nowrap;
  }

  /* Front */
  .card-front .brand {
    position: absolute;
    right: 40px;
    top: 128px;
  }
  .card-front .brand-name { font-size: 25px; }
  .tagline {
    position: absolute;
    right: 40px;
    top: 222px;
    font-size: 14px;
    letter-spacing: 0.02em;
    color: var(--ink-light);
  }

  /* Back */
  .card-back .brand {
    position: absolute;
    left: 40px;
    top: 54px;
  }
  .card-back .brand-name { font-size: 23px; }
  .person {
    position: absolute;
    left: 40px;
    top: 112px;
  }
  .person-name {
    color: var(--brand-blue);
    font-weight: 700;
    font-style: italic;
    font-size: 18px;
    text-transform: uppercase;
    letter-spacing: 0.03em;
  }
  .person-role {
    font-size: 14px;
    color: var(--ink-muted);
    margin-top: 2px;
  }
  .contact {
    position: absolute;
    left: 40px;
    top: 200px;
    list-style: none;
    font-size: 14px;
    line-height: 1.65;
  }
  .contact li { display: flex; align-items: center; gap: 9px; }
  .contact svg { width: 14px; height: 14px; fill: var(--brand-blue); flex: none; }
</style>
</head>
<body>

  <section class="card card-front" aria-label="Card front">
    <svg class="emblem-area" viewBox="0 0 640 366" role="img" aria-label="Large decorative brand emblem area">
      <defs>
        <radialGradient id="emblemFront" cx="0.35" cy="0.4" r="0.7">
          <stop offset="0" stop-color="var(--emblem-mid)"/>
          <stop offset="1" stop-color="var(--emblem-dark)"/>
        </radialGradient>
      </defs>
      <circle cx="50" cy="170" r="250" fill="url(#emblemFront)" stroke="var(--emblem-rim)" stroke-width="3"/>
    </svg>
    <div class="brand">
      <span class="brand-dot"></span>
      <span class="brand-name">Brightvale Electrical</span>
    </div>
    <p class="tagline">Domestic Commercial Industrial Electricians</p>
  </section>

  <section class="card card-back" aria-label="Card back">
    <svg class="emblem-area" viewBox="0 0 640 366" role="img" aria-label="Large decorative brand emblem area">
      <defs>
        <radialGradient id="emblemBack" cx="0.4" cy="0.35" r="0.7">
          <stop offset="0" stop-color="var(--emblem-mid)"/>
          <stop offset="1" stop-color="var(--emblem-dark)"/>
        </radialGradient>
      </defs>
      <circle cx="600" cy="290" r="260" fill="url(#emblemBack)" stroke="var(--emblem-rim)" stroke-width="3"/>
    </svg>
    <div class="brand">
      <span class="brand-dot"></span>
      <span class="brand-name">Brightvale Electrical</span>
    </div>
    <div class="person">
      <p class="person-name">Damian Holloway</p>
      <p class="person-role">Founder</p>
    </div>
    <ul class="contact">
      <li>
        <svg viewBox="0 0 24 24" aria-hidden="true"><path d="M6.6 10.8a15.1 15.1 0 0 0 6.6 6.6l2.2-2.2c.3-.3.7-.4 1-.2 1.1.4 2.3.6 3.6.6.6 0 1 .4 1 1V20c0 .6-.4 1-1 1A17 17 0 0 1 3 4c0-.6.4-1 1-1h3.5c.6 0 1 .4 1 1 0 1.3.2 2.5.6 3.6.1.3 0 .7-.2 1z"/></svg>
        <span>0219647381</span>
      </li>
      <li>
        <svg viewBox="0 0 24 24" aria-hidden="true"><path d="M2 5h20v14H2zm2 2v.4l8 5.2 8-5.2V7zm0 2.8V17h16V9.8l-8 5.2z"/></svg>
        <span>info@brightvaleelectrical.example.nz</span>
      </li>
      <li><span>Lic E871302</span></li>
    </ul>
  </section>

</body>
</html>
```